Park Company Mobile Application Design

We are looking for deisgn of the mobile application for the parking company. More details about the parking company you can find on the following web site: www.lumrapark.mk.
As well we attached the parking card that this company is issuing. As you may see their preferred color is green.
Attached you can find screens that we are planning to implement in the mobile application.
If you need more details please contact us on dragan@kestrel.mk.

Thanks,
Dragan Petrusev
Kestrel Group

```html
<!DOCTYPE html>
<html lang="en">
<head>
<meta charset="utf-8">
<title>Lumra Park – Mobile Application Screens</title>
<link rel="stylesheet" href="https://fonts.googleapis.com/css2?family=Poppins:wght@400;500;600&display=swap">
<style>
  :root {
    --backdrop: #0b1016;
    --green: #17a83b;
    --green-deep: #0f7d2b;
    --slate: #363e4f;
    --slate-dark: #2c3342;
    --white: #ffffff;
    --ink: #3b3f47;
    --panel: rgba(40, 96, 62, 0.85);
    --panel-foot: rgba(54, 62, 79, 0.55);
  }
  * { box-sizing: border-box; margin: 0; padding: 0; }
  html, body { width: 950px; height: 1200px; overflow: hidden; }
  body {
    background: var(--backdrop);
    font-family: "Poppins", sans-serif;
    color: var(--white);
    position: relative;
  }
  .screen {
    position: absolute;
    width: 221px;
    height: 479px;
    background: var(--green);
    overflow: hidden;
  }
  .screen--login-a { left: 91px; top: 114px; }
  .screen--login-b { left: 367px; top: 114px; }
  .screen--reset { left: 637px; top: 114px; }
  .screen--register { left: 91px; top: 647px; }
  .screen--pay-parking { left: 368px; top: 645px; }
  .screen--pay-fine { left: 637px; top: 644px; }

  .brand {
    position: absolute;
    left: 0; right: 0;
    display: flex; align-items: center; justify-content: center; gap: 7px;
    font-weight: 600; font-size: 21px; letter-spacing: 0.5px;
  }
  .brand__dot { width: 14px; height: 14px; border-radius: 50%; background: var(--white); }

  .field {
    position: absolute; left: 18px; width: 186px; height: 34px;
    background: var(--white); color: var(--ink);
    font-size: 9.5px; display: flex; align-items: center; padding-left: 16px;
  }
  .field--value { padding-left: 12px; }
  .btn {
    position: absolute; height: 35px; background: var(--slate);
    display: flex; align-items: center; justify-content: center;
    font-weight: 600; font-size: 10.5px; letter-spacing: 0.3px;
    box-shadow: 0 2px 3px rgba(0,0,0,0.25);
  }
  .btn--small { font-size: 9.5px; }
  .link { position: absolute; left: 0; right: 0; text-align: center; font-size: 10.5px; }

  .cityscape {
    position: absolute; left: 0; right: 0; bottom: 0;
    background: linear-gradient(180deg, rgba(23,168,59,0) 0%, #1b9a3a 30%, #127a2c 60%, #0f5e24 100%);
  }

  .title { position: absolute; left: 0; right: 0; text-align: center; font-weight: 600; font-size: 14px; letter-spacing: 0.5px; }
  .radio { position: absolute; left: 18px; display: flex; align-items: center; gap: 7px; font-size: 10.5px; }
  .radio__mark { width: 9px; height: 9px; border: 1.3px solid var(--white); border-radius: 50%; position: relative; }
  .radio__mark--on::after { content: ""; position: absolute; inset: 1.5px; background: var(--white); border-radius: 50%; }

  .topbar { position: absolute; left: 0; right: 0; top: 0; height: 61px; background: var(--slate); }
  .menu-btn {
    position: absolute; left: 13px; top: 16px; width: 24px; height: 17px;
    border: 1.3px solid var(--white); border-radius: 9px;
    display: flex; align-items: center; justify-content: center;
  }
  .map-btn {
    position: absolute; right: 12px; top: 19px; width: 35px; height: 17px;
    border: 1.3px solid var(--white); border-radius: 9px;
    font-size: 7px; font-weight: 600; display: flex; align-items: center; justify-content: center;
  }
  .badge {
    position: absolute; left: 65px; top: 12px; width: 92px; height: 92px;
    border-radius: 50%; background: var(--slate); border: 2px solid var(--green);
    display: flex; align-items: center; justify-content: center;
    font-weight: 600; font-size: 12px; letter-spacing: 0.3px;
  }
  .pill {
    position: absolute; left: 18px; width: 186px; height: 34px; border-radius: 17px;
    background: var(--white); color: var(--ink); font-size: 9.5px;
    display: flex; align-items: center; gap: 9px; padding-left: 2px;
  }
  .pill--center { justify-content: center; padding: 0; }
  .pill__icon {
    width: 29px; height: 29px; border-radius: 50%; background: var(--slate);
    display: flex; align-items: center; justify-content: center;
  }
  .btn--pill { left: 18px; width: 186px; border-radius: 18px; }

  .tabbar {
    position: absolute; left: 0; right: 0; bottom: 0; height: 36px; background: var(--slate);
    display: grid; grid-template-columns: 74px 61px 1fr;
  }
  .tabbar__item {
    display: flex; flex-direction: column; align-items: center; justify-content: center; gap: 2px;
    font-size: 6.8px; font-weight: 500; border-right: 1px solid var(--slate-dark);
  }
  .tabbar__item:last-child { border-right: 0; }
  .tabbar__item--active { color: var(--green); }

  .fine-details {
    position: absolute; left: 6px; width: 209px; top: 503px; height: 160px;
    top: 239px; background: var(--panel);
  }
  .fine-details__list { padding: 15px 0 0 16px; font-size: 9.5px; line-height: 22px; }
  .fine-details__row { display: grid; grid-template-columns: 75px 1fr; }
  .fine-details__more {
    position: absolute; left: 0; right: 0; bottom: 0; height: 31px; background: var(--panel-foot);
    display: flex; align-items: center; justify-content: flex-end; gap: 5px; padding-right: 9px;
    font-size: 9.5px; font-weight: 600;
  }
</style>
</head>
<body>

<!-- Login screens -->
<section class="screen screen--login-a">
  <div class="brand" style="top:76px"><span class="brand__dot"></span>LUMRA PARK</div>
  <div class="field" style="top:163px">Email</div>
  <div class="field" style="top:205px">Password</div>
  <div class="link" style="top:250px">Forgot your password?</div>
  <div class="btn" style="left:18px;top:280px;width:93px">REGISTER</div>
  <div class="btn" style="left:118px;top:280px;width:86px">LOGIN</div>
  <div class="cityscape" role="img" aria-label="Green city skyline with cars driving on a road" style="top:346px"></div>
</section>

<section class="screen screen--login-b">
  <div class="brand" style="top:76px"><span class="brand__dot"></span>LUMRA PARK</div>
  <div class="field" style="top:163px">Email</div>
  <div class="field" style="top:205px">Password</div>
  <div class="link" style="top:250px">Forgot your password?</div>
  <div class="btn" style="left:18px;top:280px;width:93px">REGISTER</div>
  <div class="btn" style="left:118px;top:280px;width:86px">LOGIN</div>
  <div class="cityscape" role="img" aria-label="Green city skyline with cars driving on a road" style="top:346px"></div>
</section>

<!-- Password reset -->
<section class="screen screen--reset">
  <div class="brand" style="top:70px"><span class="brand__dot"></span>LUMRA PARK</div>
  <div class="title" style="top:130px">PASSWORD RESET</div>
  <div class="field field--value" style="top:162px">marko.ilievski@mailbox.mk</div>
  <div class="radio" style="top:211px"><span class="radio__mark radio__mark--on"></span>Reset by email</div>
  <div class="radio" style="top:233px"><span class="radio__mark"></span>Reset by phone</div>
  <div class="btn btn--small" style="left:18px;top:261px;width:186px">SEND THE CODE</div>
  <div class="btn btn--small" style="left:18px;top:302px;width:186px">RESET THE PASSWORD</div>
  <div class="cityscape" role="img" aria-label="Green city skyline with cars driving on a road" style="top:346px"></div>
</section>

<!-- Registration -->
<section class="screen screen--register">
  <div class="brand" style="top:76px"><span class="brand__dot"></span>LUMRA PARK</div>
  <div class="field field--value" style="top:138px">marko.ilievski@mailbox.mk</div>
  <div class="field field--value" style="top:179px">Password</div>
  <div class="field field--value" style="top:221px">Confirm password</div>
  <div class="field field--value" style="top:262px">Phone number</div>
  <div class="btn" style="left:18px;top:306px;width:186px">NEXT</div>
  <div class="cityscape" role="img" aria-label="Green city skyline with cars driving on a road" style="top:350px"></div>
</section>

<!-- Pay parking -->
<section class="screen screen--pay-parking">
  <div class="topbar"></div>
  <div class="menu-btn">
    <svg width="10" height="8" viewBox="0 0 10 8"><path d="M0 1h10M0 4h10M0 7h10" stroke="#fff" stroke-width="1.3"/></svg>
  </div>
  <div class="map-btn">МАПА</div>
  <div class="badge">LUMRA PARK</div>
  <div class="pill" style="top:125px">
    <span class="pill__icon"><svg width="13" height="12" viewBox="0 0 13 12"><path d="M1 2l3.5-1 4 1.5L12 1v9l-3.5 1-4-1.5L1 11z" fill="#fff"/><path d="M4.5 1v8.5M8.5 2.5V11" stroke="#363e4f" stroke-width="0.8"/></svg></span>Зона 1
  </div>
  <div class="pill" style="top:172px">
    <span class="pill__icon"><svg width="12" height="12" viewBox="0 0 12 12"><circle cx="6" cy="6" r="5.3" fill="#fff"/><path d="M6 3v3.3l2 1.2" stroke="#363e4f" stroke-width="1.2" fill="none"/></svg></span>2
  </div>
  <div class="pill" style="top:219px">
    <span class="pill__icon"><svg width="13" height="10" viewBox="0 0 13 10"><path d="M2.5 4L3.8 1h5.4l1.3 3H12v4.5h-1.5V10h-2V8.5h-4V10h-2V8.5H1V4z" fill="#fff"/><circle cx="3.6" cy="6" r="0.9" fill="#363e4f"/><circle cx="9.4" cy="6" r="0.9" fill="#363e4f"/></svg></span>SK5555ss
  </div>
  <div class="btn btn--pill" style="top:268px">PAY PARKING</div>
  <div class="cityscape" role="img" aria-label="Green city skyline with cars driving on a road" style="top:310px;bottom:36px"></div>
  <nav class="tabbar">
    <div class="tabbar__item tabbar__item--active">
      <svg width="16" height="13" viewBox="0 0 16 13"><path d="M3 8l1.5-3.5h6L12 8v3H3z M5 11v1.5M10 11v1.5" stroke="#17a83b" fill="none" stroke-width="1"/><rect x="10.5" y="0.5" width="5" height="5" stroke="#17a83b" fill="none" stroke-width="1"/></svg>Pay Parking
    </div>
    <div class="tabbar__item">
      <svg width="14" height="13" viewBox="0 0 14 13"><rect x="0.5" y="0.5" width="10" height="8" rx="1" stroke="#fff" fill="none"/><path d="M2 3h7M2 5h4" stroke="#fff"/><rect x="5.5" y="6.5" width="8" height="6" rx="1" stroke="#fff" fill="#363e4f"/></svg>User card
    </div>
    <div class="tabbar__item">
      <svg width="14" height="13" viewBox="0 0 14 13"><path d="M7 1L13 12H1z" stroke="#fff" fill="none"/><path d="M7 5v3.5M7 9.8v1" stroke="#fff"/></svg>Report a problem
    </div>
  </nav>
</section>

<!-- Pay fine -->
<section class="screen screen--pay-fine">
  <div class="topbar"></div>
  <div class="menu-btn">
    <svg width="10" height="8" viewBox="0 0 10 8"><path d="M0 1h10M0 4h10M0 7h10" stroke="#fff" stroke-width="1.3"/></svg>
  </div>
  <div class="badge">LUMRA PARK</div>
  <div class="title" style="top:119px">PAY FINE</div>
  <div class="pill pill--center" style="top:148px">SK7316ak</div>
  <div class="btn btn--pill" style="top:192px">SUBMIT</div>
  <div class="cityscape" role="img" aria-label="Green city skyline with cars driving on a road" style="top:380px"></div>
  <div class="fine-details">
    <dl class="fine-details__list">
      <div class="fine-details__row"><dt>Parking Zone :</dt><dd>Зона 1</dd></div>
      <div class="fine-details__row"><dt>Hours :</dt><dd>4h</dd></div>
      <div class="fine-details__row"><dt>License :</dt><dd>SK7316ak</dd></div>
      <div class="fine-details__row"><dt>Date :</dt><dd>Dec 19, 2019</dd></div>
      <div class="fine-details__row"><dt>Price :</dt><dd>22</dd></div>
    </dl>
    <div class="fine-details__more">
      <svg width="10" height="10" viewBox="0 0 10 10"><circle cx="5" cy="5" r="5" fill="#fff"/><path d="M5 2.5v5M2.5 5h5" stroke="#2f6e47" stroke-width="1.4"/></svg>Additional information
    </div>
  </div>
</section>

</body>
</html>
```